Penned Folios Network Presents… PFNmerit.net

I. The purpose of the phase1 is to gain access to (and control of) scholastic academic works that had been written and authored by students, but only after they have been corrected (vetted), by education professionals and returned to the student as corrected documents. It is my goal to push the PFN Merit Annual as inducements to have students turn over these papers and receive recognition and authorship, for these intellectual works.

Target Market(s)

university students
high school students

Number of Pages Required

2 page

Font styles to use
Serif
Sans Serif

Colors

Designer to choose colors to be used in the design.

Requirements
Must have
• must include this or similar language.
• Penned Folios Network Presents…
• PFNmerit.net
• Here is the assemblage of your academic successes. We collect and archive your written academic achievements, you’re “A” graded as correct, written assignments throughout the year, and when it’s over, we amass your academic documents into a bound book… your Scholar Laurel Annual.
• You study hard and work hard all year trying to achieve the highest grades possible. At the end of the year, semester, or term you will have lasting proof to show what you did to achieve your academic excellence… and in book form too!
• Consider this the perfect gift to yourself to celebrate your ascendency and to showcase all of the hard work that you have put into getting to the next step on the ladder to success, your success.
• One good thing about this is that you don’t have to do any extra work to write your book. Once your written assignment has been reviewed, graded by an education authority and returned to you, all you do is to submit it to your registered account with us, add a brief description or special detail and we will add it to your database to build your success story.
• Our mission here is to track and highlight your academic successes. We want to honor and immortalize you through your academic “A” papers. Currently, once your term papers, research papers, writing assignments, book reports, studies, critiques, essays, theses, dissertations and the like, have been graded and returned back to you they soon become of no further value to you. But now with the Scholar Laurel Annual you have a system available to you that can and will create a lasting record or Yearbook to catalogue what molded you into the intellectual that you have become. Once your academic papers have been evaluated by the scholastic authority and graded accordingly, you only have to post or download these materials as they become available to you. As you repeat the process again and again the storehouse of your knowledge legacy grows exponentially and become more relevant and valuable as entries into your Scholar Laurel Annual.
• Imagine if you will, if there was a written record of Varnholt’s early studies and writings, from before he became the Varnholt that we know of today, or the Quellby’s early school and college writings? Just think of the value that these priceless gifts would hold today. Well you may say “but I’m not famous. Who would be interested in my schoolwork or assignments?” We can’t say for sure right now because the future is not known today. But we do know that years of study and research molded and shaped the Quellbys from their modest upbringing and that Varnholt struggled for many years trying to get his thoughts and writings accepted by the establishment before they finally realized that “e” really did equal “mc2” (e=mc2). Who Knew? But you don’t have to become famous to be relevant. What value would you place on old mementos and writings of your parents, grand or great grandparents from before Vietnam or WWIl or??? I’m sure Forebearline.net would kill to have access to these treasures. And so would your kids or descendants in future years. Yes, you are relevant and you can make a lasting difference if you create an enduring legacy. Together we can create that legacy.
• “Log on to: PFNmerit.net to comprehend what all the excitement is all about.”
• We are the vehicle to deliver your curriculum based study writings to you in the easiest and most hassle free way possible. As members of the Scholar Laurel community your papers will always be available to you. Periodically this material will be compiled, configured if necessary, and formatted into book form as your personalized Scholar Laurel Annual matures.
Nice to have
• very professional but student friendly graphes
Should not have
• leave out the affiliate program at this time.

```html
<!DOCTYPE html>
<html lang="en">
<head>
<meta charset="utf-8">
<title>Penned Folios Network — PFNmerit.net</title>
<link rel="stylesheet" href="https://fonts.googleapis.com/css2?family=Open+Sans:wght@300;400;600;700&display=swap">
<style>
:root{
  --stage:#e3e3e3;
  --white:#ffffff;
  --paper:#f2f2f2;
  --ink:#555555;
  --ink-dark:#333333;
  --blue:#29a9e1;
  --blue-light:#5cc3ef;
  --blue-deep:#0b6794;
  --blue-footer:#3ba7dd;
  --blue-bar:#1778ad;
  --grey-btn:#9a9a9a;
  --row:#ececec;
}
*{box-sizing:border-box;margin:0;padding:0}
html,body{width:1200px;height:2473px;overflow:hidden}
body{background:var(--stage);font-family:"Open Sans",Arial,sans-serif;color:var(--ink);position:relative}
.page{position:absolute;left:145px;top:66px;width:920px;height:2335px;background:var(--paper);overflow:hidden}
.abs{position:absolute}

/* header */
.site-header{left:0;top:0;width:920px;height:89px;background:var(--white)}
.brand{left:122px;top:24px;display:flex;align-items:center;gap:6px}
.brand-dot{width:46px;height:46px;border-radius:50%;background:var(--blue);flex:none}
.brand-name{font-size:17px;font-weight:600;color:var(--blue);white-space:nowrap}
.account{right:120px;top:30px;font-size:9px;font-weight:700;color:var(--blue);display:flex;align-items:center;gap:6px}
.nav-item{top:58px;font-size:10px;color:var(--ink-dark);white-space:nowrap}
.nav-item.active{left:287px;top:53px;width:50px;text-align:center;color:var(--blue);border-top:3px solid var(--blue);padding-top:2px}
.search-label{left:564px;top:60px;font-size:7.5px;font-weight:700;color:var(--ink-dark);white-space:nowrap}
.search-box{left:627px;top:57px;width:132px;height:15px;background:#eeeeee;font-size:7.5px;color:#aaa;padding:1px 6px;white-space:nowrap;overflow:hidden}
.search-btn{left:765px;top:57px;width:32px;height:15px;background:var(--blue)}

/* hero */
.hero{left:0;top:89px;width:920px;height:536px;clip-path:polygon(0 0,100% 0,100% 97.5%,50% 100%,0 97.8%);
  background:radial-gradient(ellipse at 42% 30%,#8c8c8c 0%,#5a5a5a 45%,#2b2b2b 100%)}
.hero-title{left:0;top:306px;width:920px;text-align:center;font-size:53px;font-weight:300;color:var(--white);letter-spacing:-1.5px;line-height:1.1;white-space:nowrap}
.hero-title b{font-weight:600}
.hero-sub{left:0;top:377px;width:920px;text-align:center;font-size:14px;font-weight:600;color:var(--white);letter-spacing:-.5px;white-space:nowrap}
.btn{height:43px;display:flex;align-items:center;justify-content:center;font-size:12px;color:var(--white);letter-spacing:-.3px}
.btn-archive{left:292px;top:432px;width:160px;background:#2a86b3;border-bottom:3px solid var(--blue)}
.btn-view{left:461px;top:432px;width:158px;background:var(--grey-btn);border-bottom:3px solid #cfcfcf}

.badge{left:412px;top:583px;width:99px;height:99px;border-radius:50%;background:var(--white);border:3px solid #222}

/* intro */
.intro-title{left:122px;top:749px;width:345px;font-size:16px;font-weight:700;color:#4a4a4a;line-height:1.25;letter-spacing:-.2px}
.intro-text{left:122px;top:808px;width:335px;font-size:10.5px;line-height:19px;color:var(--ink);letter-spacing:-.2px}
.video{left:508px;top:732px;width:288px;height:204px;background:linear-gradient(135deg,#4fb8e6,#2a9fd6)}
.figure-blob{left:160px;top:997px;width:577px;height:363px}

/* band */
.band{left:0;top:1330px;width:920px;height:400px}
.quote-mark{left:118px;top:1388px;font-size:80px;font-weight:700;color:var(--white);line-height:1;font-family:Georgia,serif}
.band-text{left:122px;top:1468px;width:285px;font-size:11px;line-height:18px;color:var(--white)}
.signup{left:122px;top:1627px;width:104px;height:25px;background:var(--white);color:var(--ink-dark);font-size:10px;display:flex;align-items:center;justify-content:center;box-shadow:1px 2px 2px rgba(0,0,0,.25)}
.pill{height:25px;border-radius:13px;background:var(--blue);color:var(--white);font-size:12px;font-weight:600;padding:4px 11px;white-space:nowrap}
.pill.c1{left:488px;width:135px}
.pill.c2{left:638px;width:145px}

/* faq */
.faq-heading{left:0;top:1741px;width:920px;text-align:center;font-size:19px;font-weight:700;color:var(--blue);line-height:28px}
.faq-rule{top:1755px;width:56px;height:1px;background:var(--blue)}
.faq{left:198px;top:1791px;width:527px}
.faq-open{height:30px;background:var(--blue);color:var(--white);font-size:12px;font-weight:700;display:flex;align-items:center;padding-left:12px;gap:12px;white-space:nowrap}
.faq-body{background:var(--white);height:64px;font-size:10.5px;font-weight:700;color:#2e2e2e;line-height:1.15;padding:10px 140px 9px 15px}
.faq-row{margin-top:5px;height:28px;background:var(--row);font-size:11.5px;color:#777;display:flex;align-items:center;padding-left:10px;gap:12px;white-space:nowrap}
.faq-row.first{margin-top:1px}
.sign{font-size:20px;font-weight:400;line-height:1;width:12px;text-align:center}

/* footer */
.footer{left:0;top:2073px;width:920px;height:211px;background:linear-gradient(180deg,#4db3e6,var(--blue-footer))}
.contact{left:122px;font-size:10.5px;color:var(--white);display:flex;align-items:center;gap:6px}
.support-label{left:488px;top:2102px;font-size:11px;color:var(--white)}
.field{left:488px;width:265px;border:1px solid rgba(255,255,255,.7)}
.submit{left:490px;top:2246px;width:102px;height:26px;background:var(--white);font-size:10px;color:var(--ink-dark);display:flex;align-items:center;justify-content:center}
.footer-bar{left:0;top:2284px;width:920px;height:51px;background:var(--blue-bar)}
.footer-brand{left:66px;top:2295px;display:flex;align-items:center;gap:6px}
.footer-brand .brand-dot{width:28px;height:28px;background:var(--white)}
.footer-brand .brand-name{font-size:13px;color:var(--white)}
.social{left:741px;top:2302px;display:flex;gap:6px;align-items:center;font-size:9px;color:var(--white)}
.social i{width:14px;height:14px;border:1.5px solid var(--white);border-radius:50%;display:block}
</style>
</head>
<body>
<div class="page">

  <header class="abs site-header">
    <div class="abs brand"><span class="brand-dot"></span><span class="brand-name">PFNmerit.net</span></div>
    <div class="abs account">LOGIN &nbsp;|&nbsp; REGISTER
      <svg width="18" height="14" viewBox="0 0 18 14"><circle cx="7" cy="4" r="3.2" fill="none" stroke="#29a9e1" stroke-width="1.3"/><path d="M1 13c0-4 12-4 12 0" fill="none" stroke="#29a9e1" stroke-width="1.3"/><path d="M15 6l1.5 1.5L18 6" fill="none" stroke="#29a9e1"/></svg>
    </div>
    <nav>
      <span class="abs nav-item active">Home</span>
      <span class="abs nav-item" style="left:356px">How It Works</span>
      <span class="abs nav-item" style="left:445px">FAQs</span>
      <span class="abs nav-item" style="left:494px">Contact Us</span>
    </nav>
    <div class="abs search-label">SEARCH PAPER</div>
    <div class="abs search-box">e.g. local education...</div>
    <div class="abs search-btn"><svg width="32" height="15" viewBox="0 0 32 15"><circle cx="15" cy="6.5" r="3.5" fill="none" stroke="#fff" stroke-width="1.4"/><path d="M17.5 9l2.5 2.5" stroke="#fff" stroke-width="1.6"/></svg></div>
  </header>

  <section class="abs hero" role="img" aria-label="Black and white photo of a smiling graduate in cap in front of a campus building"></section>
  <h1 class="abs hero-title"><b>Penned Folios</b> Network</h1>
  <p class="abs hero-sub">Your online accademic success assemblage portal, a perfect gift to yourself</p>
  <div class="abs btn btn-archive">Archive now</div>
  <div class="abs btn btn-view">View your success</div>

  <div class="abs badge" role="img" aria-label="Illustration of a graded A+ paper"></div>

  <h2 class="abs intro-title">Your online accademic success assemblage portal, a perfect gift to yourself</h2>
  <p class="abs intro-text">Here is the assemblage of your academic successes. We collect and archive your written academic achievements, you’re “A” graded as correct, written assignments throughout the year, and when it’s over, we amass your academic documents into a bound book… your Scholar Laurel Annual.</p>
  <div class="abs video" role="img" aria-label="Video preview illustration of a student reading a book">
    <svg width="288" height="204" viewBox="0 0 288 204"><circle cx="144" cy="98" r="24" fill="none" stroke="#fff" stroke-width="3"/><path d="M137 86v24l19-12z" fill="none" stroke="#fff" stroke-width="3" stroke-linejoin="round"/></svg>
  </div>

  <svg class="abs figure-blob" viewBox="0 0 577 363" role="img" aria-label="Photo of two smiling graduates with flower leis and diplomas, framed by soft blue shapes">
    <defs><linearGradient id="blobBlue" x1="0" y1="0" x2="1" y2="1"><stop offset="0" stop-color="#9fd9f3"/><stop offset="1" stop-color="#29a9e1"/></linearGradient></defs>
    <path d="M30 150c20-70 120-80 200-60s190-60 200 20c8 70 40 120 20 200l-450 10c-30-70 10-110 30-170z" fill="#e4e4e4"/>
    <path d="M70 120c30-80 140-60 180-20s130-40 170 10c50 60 70 140 40 250H60C20 290 50 180 70 120z" fill="url(#blobBlue)"/>
    <path d="M150 70c20-40 90-60 160-30s60 90 40 160-10 110-40 160H150c-40-90-30-180 0-290z" fill="#7c8a96" opacity=".85"/>
  </svg>

  <svg class="abs band" viewBox="0 0 920 400" preserveAspectRatio="none" aria-hidden="true">
    <defs><linearGradient id="bandGrad" x1="0" y1="0" x2="1" y2="0"><stop offset="0" stop-color="#5cc3ef"/><stop offset=".5" stop-color="#2a98d0"/><stop offset="1" stop-color="#0b6794"/></linearGradient></defs>
    <path d="M0 5L460 30L920 5V392L0 370Z" fill="url(#bandGrad)"/>
  </svg>
  <div class="abs quote-mark">“</div>
  <p class="abs band-text">Lorem ipsum dolor sit amet, consectetur adipiscing elit, sed do eiusmod tempor incididunt ut labore et dolore magna aliqua. Ut enim ad minim veniam, quis nostrud exercitation ullamco laboris nisi ut aliquip ex ea commodo consequat. Duis aute irure dolor in reprehenderit in voluptate velit esse cillum doloremollit anim id est laborum.</p>
  <div class="abs signup">Signup Now!</div>

  <div class="abs pill c1" style="top:1451px">Research Papers</div>
  <div class="abs pill c2" style="top:1451px">Critiques</div>
  <div class="abs pill c1" style="top:1492px">Term papers</div>
  <div class="abs pill c2" style="top:1492px">Writing Assignments</div>
  <div class="abs pill c1" style="top:1532px">Book Reports</div>
  <div class="abs pill c2" style="top:1532px">Essays</div>
  <div class="abs pill c1" style="top:1573px">Studies</div>
  <div class="abs pill c2" style="top:1573px">Theses</div>
  <div class="abs pill c1" style="top:1613px">Dissertations</div>

  <h2 class="abs faq-heading">FAQs</h2>
  <span class="abs faq-rule" style="left:371px"></span>
  <span class="abs faq-rule" style="left:494px"></span>

  <div class="abs faq">
    <div class="faq-open"><span class="sign">–</span>Lorem ipsum dolor sit amet, consectetur adipiscing elit,</div>
    <div class="faq-body">Lorem ipsum dolor sit amet, consectetur adipiscing elit, sed do eiusmod tempLorem ipsum dolor sit amet, consectetur adipiscing elit, sed do eiusmod temp Lorem ipsum dolor sit</div>
    <div class="faq-row first"><span class="sign">+</span>Lorem ipsum dolor sit amet, consectetur adipiscing elit, sed</div>
    <div class="faq-row"><span class="sign">+</span>Lorem ipsum dolor sit amet, consectetur adipiscing elit, sed</div>
    <div class="faq-row"><span class="sign">+</span>Lorem ipsum dolor sit amet, consectetur adipiscing elit, sed</div>
    <div class="faq-row"><span class="sign">+</span>Lorem ipsum dolor sit amet, consectetur adipiscing elit, sed</div>
  </div>

  <footer>
    <div class="abs footer" role="img" aria-label="Blue-tinted photo of graduates tossing caps in celebration"></div>
    <div class="abs contact" style="top:2142px">
      <svg width="14" height="10" viewBox="0 0 14 10"><rect x=".5" y=".5" width="13" height="9" fill="none" stroke="#fff"/><path d="M.5 .5L7 6l6.5-5.5" fill="none" stroke="#fff"/></svg>info@pfnmerit.net</div>
    <div class="abs contact" style="top:2168px">
      <svg width="14" height="14" viewBox="0 0 14 14"><path d="M3 1l2 3-1.5 1.5c1 2 3 4 5 5L10 9l3 2-1.5 2.5C6 13 1 8 .5 2.5z" fill="#fff"/></svg>+1234567890,</div>
    <div class="abs contact" style="top:2197px">
      <svg width="14" height="14" viewBox="0 0 14 14"><path d="M7 13S2 7.5 2 5a5 5 0 0110 0c0 2.5-5 8-5 8z" fill="#fff"/><circle cx="7" cy="5" r="1.8" fill="#3ba7dd"/></svg>Address...</div>

    <div class="abs support-label">GET SUPPORT</div>
    <div class="abs field" style="top:2124px;height:19px"></div>
    <div class="abs field" style="top:2147px;height:18px"></div>
    <div class="abs field" style="top:2170px;height:68px"></div>
    <div class="abs submit">Submit</div>

    <div class="abs footer-bar"></div>
    <div class="abs footer-brand"><span class="brand-dot"></span><span class="brand-name">PFNmerit.net</span></div>
    <div class="abs social"><i></i><i></i><i></i><span>C 2018</span></div>
  </footer>
</div>
</body>
</html>
```